brighter morrow needs graphic design for label

I need a label to describe a new product which is organically grown free from chemicals & sprays, The product contains powerful combination of Aloe & herbs that are antibiotic, antibacterial, antiviral, antioxidant, (fights free-radicals). Therefore, assists the body to rid itself of toxins, increases oxygen levels in the cells, builds immune system allowing healing to take place in all areas of damage or disease, Healing will be seen from one to three months. Grown, produced, packaged in Australia by a small family business. Instruction should be on label for dose, frequency, length of usage; when not to use ect. It will be contained in a small 150ml navy blue glass bottle. I would like label to have black background with some color in it. Instruction should be on label for dose ( start with 5ml x 3 daily). As body transitions from detox to healing have short break then continue increasing dose until desired healing effect takes place.

The plant & herbs also contain all the nutrients required for daily activities /healthy life-style
I am willing to pay extra for a good logo for, "brighter morrow", which is to go on the bottle

Size will be approx. 7 cm x 10cm
 i have only stated the information required, however, I have not got an organised structure.
I am waiting for a bar code

These are the information to be given on label:
Waking Calm in Tissue ( this will make a good name for the product)
Company name with logo (In progress of being created) Discription of product saying......
Supreme therapeutic herbal & plant cocktail creating a potent internal detox; aiding digestion, promoting cell repair.
Many other health benefits including......
Actions:  antibiotic, antioxident, diuetic, anti-inflammatory, anti-rheumatism, anti-arthiritis, antidiabetic, assisst with blood pressure.
 stabalising.
Organically grown & produced by small Australian family. No chemicals, sprays, or artificial preservatives.
presereved in raw pure honey organicall produced.  Containes honey, aloe aborescence, infused with properties & nutients of Herb Robert & stinnging nettle.

Target Market(s)

most ages who are sick,suffering illness, disease, or just to improve overall health

Industry/Entity Type

Graphic Design

Requirements
Nice to have
• Not sure.

```html
<!DOCTYPE html>
<html lang="en">
<head>
<meta charset="utf-8">
<title>brighter morrow – label</title>
<link rel="stylesheet" href="https://fonts.googleapis.com/css2?family=Arimo:wght@400;700&family=Tenor+Sans&family=Great+Vibes&display=swap">
<style>
  :root {
    --page: #ffffff;
    --label-black: #0c0c0c;
    --leaf-shadow: #2f2c2c;
    --ink-white: #ffffff;
    --leaf-lime: #8dc21f;
    --leaf-green: #1f9a3c;
    --leaf-deep: #0a5a2a;
    --leaf-teal: #0b8060;
  }
  * { margin: 0; padding: 0; box-sizing: border-box; }
  html, body { width: 1200px; height: 1000px; overflow: hidden; background: var(--page); }
  .canvas { position: relative; width: 1200px; height: 1000px; }
  .label {
    position: absolute; left: 285px; top: 65px; width: 622px; height: 888px;
    background: var(--label-black); overflow: hidden; color: var(--ink-white);
    font-family: "Arimo", Arial, sans-serif;
  }
  .backdrop-leaves {
    position: absolute; left: 0; top: 120px; width: 622px; height: 520px;
    background: radial-gradient(ellipse at 45% 45%, var(--leaf-shadow) 0%, #1c1a1a 45%, var(--label-black) 80%);
    opacity: 0.9;
  }
  .description {
    position: absolute; left: 0; top: 32px; width: 100%;
    text-align: center; font-weight: 700; font-size: 20px; line-height: 29px;
  }
  .brand-name {
    position: absolute; left: 0; top: 272px; width: 100%; text-align: center;
    font-family: "Tenor Sans", "Trebuchet MS", sans-serif; font-variant: small-caps;
    font-size: 118px; line-height: 104px; letter-spacing: 1px; color: var(--ink-white);
  }
  .meadow {
    position: absolute; left: 58px; top: 508px; width: 545px; height: 168px;
    background: linear-gradient(100deg, var(--leaf-green) 0%, var(--leaf-lime) 22%, var(--leaf-green) 45%, var(--leaf-deep) 65%, var(--leaf-teal) 100%);
    border-radius: 50% 50% 60% 40% / 30% 30% 70% 70%;
  }
  .tagline {
    position: absolute; left: 0; top: 526px; width: 100%; text-align: center; padding-right: 30px;
    font-family: "Great Vibes", cursive; font-size: 30px; color: var(--ink-white);
  }
  .dose {
    position: absolute; left: 0; top: 686px; width: 100%; text-align: center;
    font-weight: 700; font-size: 20px;
  }
  .benefits {
    position: absolute; left: 110px; top: 718px; width: 400px; text-align: center;
    font-size: 14px; line-height: 17px;
  }
  .origin {
    position: absolute; left: 70px; top: 800px; width: 480px; text-align: center;
    font-weight: 700; font-size: 13.5px; line-height: 17px;
  }
</style>
</head>
<body>
<div class="canvas">
  <section class="label">
    <div class="backdrop-leaves" role="img" aria-label="Faint large dark grey leaf silhouettes behind the product name"></div>
    <p class="description">Supreme therapeutic herbal &amp;<br>plant cocktail creating a potent internal<br>detox; aidng digestion, promoting cell repair.</p>
    <h1 class="brand-name">brighter<br>morrow</h1>
    <div class="meadow" role="img" aria-label="Stylised green hills and overlapping leaves in lime, green and teal"></div>
    <p class="tagline">Waking Calm in Tissue</p>
    <p class="dose">start with 5ml x 3 daily</p>
    <p class="benefits">Many other health benefits including......<br>Actions:&nbsp; antibiotic, antioxident, diuetic, anti-inflammatory, anti-rheumatism, anti-arthiritis, antidiabetic, assisst with blood pressure.</p>
    <p class="origin">Organically grown &amp; produced by small Australian family. No chemicals, sprays, or artificial preservatives. preserved in raw pure honey organicall produced.&nbsp; Contains honey, aloe aborscence, infused with properties &amp; nutients of Herb Robert &amp; stinging nettle.</p>
  </section>
</div>
</body>
</html>
```